Online store for a printing company

we are a printing company and want a webshop in spotify.
With our full catalog, customer login, online payments, choices of paper types etc.

https://www.velmora.be --> like this one, we have the same products/catalogus so you can take them.

Ofcourse you don't need to add all the 500 products. But if you add like 30-50 we will add the rest.

our current site is; www.lindevaart.be

Target Market(s)

B2B / B2C

Requirements
Must have
• *full catalog
*costumer login
*online payments
Nice to have
• products in the picture banner

```html
<!DOCTYPE html>
<html lang="en">
<head>
<meta charset="utf-8">
<title>Lindevaart – Printing &amp; graphic agency</title>
<link rel="stylesheet" href="https://fonts.googleapis.com/css2?family=Fira+Sans:wght@500;600;700&family=Merriweather:wght@700;900&family=Lato:wght@400;700&display=swap">
<style>
:root{
  --ink:#222;
  --muted:#555;
  --blue:#21678f;
  --line:#dcdcdc;
  --pale:#efefef;
  --white:#fff;
  --black:#111;
}
*{box-sizing:border-box;margin:0;padding:0}
html,body{width:1200px;height:4792px;overflow:hidden}
body{position:relative;background:var(--white);font-family:'Lato',sans-serif;color:var(--ink)}
.abs{position:absolute}

.topbar{left:0;top:0;width:1200px;height:52px;background:var(--pale);font:700 11px 'Merriweather',serif;text-align:center;line-height:52px;letter-spacing:.3px}
.header{left:0;top:52px;width:1200px;height:168px;border-bottom:1px solid var(--line)}
.header-rule{left:0;top:60px;width:1200px;height:1px;background:var(--line)}
.brand{left:70px;top:18px;width:142px;height:142px;border-radius:50%;background:var(--black);border:4px solid var(--white);box-shadow:0 0 0 2px var(--black);color:var(--white);display:flex;flex-direction:column;align-items:center;justify-content:center}
.brand-name{font:700 22px 'Fira Sans',sans-serif}
.brand-sub{font:500 9px 'Fira Sans',sans-serif;margin-top:4px}
.utility{top:24px;font:700 10px 'Merriweather',serif;display:flex;gap:28px}
.contact{top:22px;font:700 12px 'Merriweather',serif;display:flex;gap:40px;right:74px}
.contact span{display:flex;align-items:center;gap:6px}
.nav{left:306px;top:107px;display:flex;gap:30px;font:700 12px 'Merriweather',serif}
.nav .active{color:var(--blue)}
.icon-btn{top:96px;width:34px;height:34px;border:1px solid #bbb;border-radius:50%;display:flex;align-items:center;justify-content:center}
.search{left:918px;top:95px;width:208px;height:40px;border:1px solid #ccc;font-size:13px;color:var(--muted);padding:0 12px;display:flex;align-items:center;justify-content:space-between}

.hero{left:0;top:220px;width:1200px;height:533px;background:linear-gradient(90deg,#eef1f2 0%,#e6eaec 55%,#dfe3e5 100%)}
.hero-photo{left:640px;top:0;width:560px;height:533px;background:radial-gradient(ellipse at 55% 45%,#e8dcc8 0%,#d9cdb8 35%,#b6c7d6 55%,#e3e7ea 80%)}
.hero-title{left:75px;top:150px;font:700 50px/54px 'Fira Sans',sans-serif;color:var(--blue);letter-spacing:.5px}
.hero-sub{left:75px;top:262px;font:600 26px 'Fira Sans',sans-serif;color:var(--ink)}
.btn{background:var(--blue);color:var(--white);font:700 15px 'Merriweather',serif;display:flex;align-items:center;justify-content:center}
.hero-btn{left:75px;top:323px;width:156px;height:52px}
.arrow-dot{width:36px;height:36px;border-radius:50%;background:#333;display:flex;align-items:center;justify-content:center;top:247px}

.tile{overflow:hidden}
.tile-label{position:absolute;background:rgba(255,255,255,.9);text-align:center;padding-top:12px}
.tile-label h3{font:600 31px 'Fira Sans',sans-serif}
.tile-label p{font:700 13px 'Lato',sans-serif;margin-top:8px}

.section-title{font:700 28px 'Merriweather',serif;letter-spacing:.3px}
.pager{width:30px;height:30px;background:#444;display:flex;align-items:center;justify-content:center}
.card{border:1px solid var(--line);background:var(--white)}
.card-media{position:absolute;left:18px;top:18px;width:204px;height:200px}
.card h4{position:absolute;left:18px;top:232px;font:700 18px 'Merriweather',serif}
.card .desc{position:absolute;left:18px;top:262px;font-size:15px;color:var(--muted)}
.card .price{position:absolute;left:18px;top:290px;font:700 15px 'Merriweather',serif;color:var(--blue)}

.banner{left:0;top:2100px;width:1200px;height:405px;background:linear-gradient(180deg,#3a3a3a,#555 55%,#3f3f3f)}
.banner h2{position:absolute;left:0;width:1200px;top:138px;text-align:center;color:var(--white);font:700 45px/56px 'Merriweather',serif}

.post{border:1px solid var(--line)}
.post-media{position:absolute;left:0;top:0;width:100%;height:206px}
.post h4{position:absolute;left:24px;top:234px;font:700 21px 'Merriweather',serif}
.post-meta{position:absolute;left:0;top:290px;width:100%;height:70px;border-top:1px solid var(--line);display:flex;align-items:center;justify-content:space-between;padding:0 36px 0 24px;font-size:12.5px;color:var(--muted)}
.post-meta span{display:flex;align-items:center;gap:16px}

.map{left:0;top:3519px;width:1200px;height:443px;background:linear-gradient(135deg,#eaeceb,#f2f1ec 45%,#e6ece6)}
.loc{left:74px;top:3575px;width:331px;height:325px;background:var(--white);box-shadow:0 2px 10px rgba(0,0,0,.25);border-radius:6px;text-align:center}
.loc h3{margin-top:36px;font:700 24px 'Merriweather',serif;letter-spacing:.5px}
.loc .q{margin-top:30px;font-size:13px;color:var(--ink)}
.loc .link{margin-top:22px;font-size:14px;color:var(--blue)}
.loc .note{margin-top:18px;font-size:13.5px;line-height:30px}
.loc .btn{width:160px;height:42px;margin:22px auto 0;background:var(--black);font-size:12px}

.news{left:0;top:3962px;width:1200px;height:307px;background:linear-gradient(180deg,#4a4a48,#5b5a57 50%,#3f3e3c)}
.news h2{position:absolute;top:92px;width:1200px;text-align:center;color:var(--white);font:700 26px 'Merriweather',serif}
.news p{position:absolute;top:142px;width:1200px;text-align:center;color:#f0f0f0;font-size:17px}
.news-field{left:318px;top:4176px;width:512px;height:48px;background:var(--white);font-size:13px;padding-left:18px;display:flex;align-items:center}
.news-go{left:830px;top:4176px;width:56px;height:48px;background:var(--blue)}

.perks{left:0;top:4269px;width:1200px;height:136px;border-top:1px solid var(--line);border-bottom:1px solid var(--line);display:flex}
.perk{flex:0 0 270px;border-right:1px solid var(--line);display:flex;align-items:center;justify-content:space-between;padding:0 40px 0 26px;font:700 13px/22px 'Merriweather',serif;color:var(--blue)}
.perk:first-child{flex:0 0 330px;padding-left:74px}
.perk:last-child{border-right:none;flex:1}

.foot-col h5{font:700 21px 'Merriweather',serif;margin-bottom:22px}
.foot-col li{list-style:none;font-size:14px;line-height:32px}
.foot-col p{font-size:14px;line-height:32px}
.foot-field{width:422px;height:48px;border:1px solid #ccc;display:flex;align-items:center;padding-left:18px;font-size:13px;position:relative}
.foot-field .go{position:absolute;right:-1px;top:-1px;width:62px;height:48px;background:var(--black);display:flex;align-items:center;justify-content:center}
.social{display:flex;gap:22px;margin-top:30px}
.social i{width:16px;height:16px;border-radius:50%;background:#999;display:block}

.bottombar{left:0;top:4706px;width:1200px;height:86px;background:var(--pale);font-size:12px;display:flex;align-items:center;justify-content:space-between;padding:0 75px 0 75px}
.pay{display:flex;gap:14px}
.pay i{display:block;width:34px;height:22px;background:#555;border-radius:2px}
</style>
</head>
<body>

<div class="abs topbar">MINIMUM ORDER $30 | FREE DELIVERY ON ORDERS OVER $100</div>

<header class="abs header">
  <div class="abs header-rule"></div>
  <div class="abs brand"><div class="brand-name">Lindevaart</div><div class="brand-sub">printing &amp; graphics</div></div>
  <div class="abs utility" style="left:253px">
    <span>MY ACCOUNT</span><span>ABOUT</span><span>CONTACT US</span>
  </div>
  <div class="abs contact">
    <span><svg width="12" height="12" viewBox="0 0 24 24"><path fill="#21678f" d="M6.6 10.8a15 15 0 006.6 6.6l2.2-2.2c.3-.3.7-.4 1-.2 1.1.4 2.3.6 3.6.6.6 0 1 .4 1 1V20c0 .6-.4 1-1 1A17 17 0 013 4c0-.6.4-1 1-1h3.5c.6 0 1 .4 1 1 0 1.3.2 2.5.6 3.6.1.3 0 .7-.2 1z"/></svg>1-800-555-0142</span>
    <span><svg width="13" height="11" viewBox="0 0 24 18"><path fill="#21678f" d="M0 0h24v2L12 10 0 2zM0 4l12 8 12-8v14H0z"/></svg>hello@lindevaart.be</span>
  </div>
  <nav class="abs nav">
    <span class="active">HOME</span><span>WOMEN</span><span>MEN</span><span>ABOUT</span><span>CONTACT</span><span>CATALOG</span>
  </nav>
  <div class="abs icon-btn" style="left:805px"><svg width="14" height="14" viewBox="0 0 24 24"><circle cx="12" cy="7" r="5" fill="#111"/><path d="M2 24c0-6 4-9 10-9s10 3 10 9z" fill="#111"/></svg></div>
  <div class="abs icon-btn" style="left:855px"><svg width="14" height="14" viewBox="0 0 24 24"><path d="M1 2h4l3 13h12l3-9H7" fill="none" stroke="#111" stroke-width="2.5"/><circle cx="9" cy="20" r="2" fill="#111"/><circle cx="18" cy="20" r="2" fill="#111"/></svg></div>
  <div class="abs search">Search<svg width="14" height="14" viewBox="0 0 24 24"><circle cx="10" cy="10" r="7" fill="none" stroke="#222" stroke-width="3"/><path d="M15 15l7 7" stroke="#222" stroke-width="3"/></svg></div>
</header>

<section class="abs hero">
  <div class="abs hero-photo" role="img" aria-label="Photo of a woman wearing a printed floral face mask"></div>
  <h1 class="abs hero-title">WELCOME TO<br>LINDEVAART</h1>
  <div class="abs hero-sub">Printing &amp; graphic agency</div>
  <div class="abs btn hero-btn">SHOP NOW</div>
  <div class="abs arrow-dot" style="left:22px"><svg width="14" height="14" viewBox="0 0 24 24"><path d="M16 3L7 12l9 9" fill="none" stroke="#fff" stroke-width="4"/></svg></div>
  <div class="abs arrow-dot" style="left:1140px"><svg width="14" height="14" viewBox="0 0 24 24"><path d="M8 3l9 9-9 9" fill="none" stroke="#fff" stroke-width="4"/></svg></div>
</section>

<div class="abs tile" style="left:74px;top:805px;width:512px;height:341px;background:linear-gradient(135deg,#cfd3d6,#e9eaea 50%,#b9b3a9)" role="img" aria-label="Photo of a sheet of printed stickers">
  <div class="tile-label" style="left:38px;top:228px;width:440px;height:90px"><h3>Stickers</h3><p>Aliquam mollis porttitor ante ut faucibus.</p></div>
</div>
<div class="abs tile" style="left:614px;top:805px;width:511px;height:341px;background:linear-gradient(160deg,#5b2a10,#a24e1b 45%,#7d4f2c 75%,#8f8a84)" role="img" aria-label="Photo of a stack of printed envelopes on a wooden table">
  <div class="tile-label" style="left:38px;top:228px;width:440px;height:90px"><h3>Cards &amp; Invitations</h3><p>Aliquam mollis porttitor ante ut faucibus.</p></div>
</div>
<div class="abs tile" style="left:74px;top:1179px;width:331px;height:400px;background:linear-gradient(135deg,#1d2025,#2e3742 55%,#6fb6cf)" role="img" aria-label="Photo of business cards on a dark surface">
  <div class="tile-label" style="left:20px;top:282px;width:290px;height:88px"><h3>Office Supplies</h3><p>Aliquam mollis porttitor ante.</p></div>
</div>
<div class="abs tile" style="left:435px;top:1179px;width:330px;height:400px;background:linear-gradient(135deg,#2d4f7b,#587aa0 45%,#b9b2a3)" role="img" aria-label="Photo of hands sorting printed sheets">
  <div class="tile-label" style="left:20px;top:282px;width:290px;height:88px"><h3>Promotion</h3><p>Aliquam mollis porttitor ante.</p></div>
</div>
<div class="abs tile" style="left:794px;top:1179px;width:331px;height:400px;background:linear-gradient(135deg,#1b1b1b,#3a3a3a 50%,#8a8179)" role="img" aria-label="Photo of a screen printing frame being lifted">
  <div class="tile-label" style="left:24px;top:282px;width:284px;height:88px"><h3>Business Gifts</h3><p>Aliquam mollis porttitor ante.</p></div>
</div>

<h2 class="abs section-title" style="left:74px;top:1632px">FEATURED PRODUCTS</h2>
<div class="abs pager" style="left:1096px;top:1637px"><svg width="10" height="10" viewBox="0 0 24 24"><path d="M16 3L7 12l9 9" fill="none" stroke="#fff" stroke-width="4"/></svg></div>

<div class="abs card" style="left:74px;top:1698px;width:242px;height:331px">
  <div class="card-media" style="top:58px;height:126px;background:linear-gradient(90deg,#1a1a1a 35%,#f2f2f2 35%)" role="img" aria-label="Business card design mockup"></div>
  <h4>Product Heading</h4><div class="desc">Nulla luctus eget</div><div class="price">$10.00</div>
</div>
<div class="abs card" style="left:344px;top:1698px;width:242px;height:331px">
  <div class="card-media" style="left:50px;width:142px;background:linear-gradient(180deg,#2a2f3a,#c8312f 55%,#2a2f3a)" role="img" aria-label="Printed flyer design"></div>
  <h4>Product Heading</h4><div class="desc">Nulla luctus eget</div><div class="price">$10.00</div>
</div>
<div class="abs card" style="left:614px;top:1698px;width:242px;height:331px">
  <div class="card-media" style="left:90px;width:60px;background:linear-gradient(180deg,#dfe9f2,#1f5fb0 45%,#e5eef6)" role="img" aria-label="Bottle of hand sanitiser with printed label"></div>
  <h4>Product Heading</h4><div class="desc">Nulla luctus eget</div><div class="price">$10.00</div>
</div>
<div class="abs card" style="left:884px;top:1698px;width:241px;height:331px">
  <div class="card-media" style="top:60px;height:110px;background:linear-gradient(135deg,#e0a92a,#f1c84a 50%,#b9892c)" role="img" aria-label="Face mask with printed yellow floral pattern"></div>
  <h4>Product Heading</h4><div class="desc">Nulla luctus eget</div><div class="price">$10.00</div>
</div>

<section class="abs banner" role="img" aria-label="Photo of a print shop worker handling printed sheets">
  <h2>Etiam convallis augue vitae massa<br>porttitor iaculis</h2>
</section>

<h2 class="abs section-title" style="left:74px;top:2552px">RECOMMENDED FOR YOU</h2>
<div class="abs pager" style="left:1096px;top:2557px"><svg width="10" height="10" viewBox="0 0 24 24"><path d="M16 3L7 12l9 9" fill="none" stroke="#fff" stroke-width="4"/></svg></div>

<div class="abs card" style="left:74px;top:2619px;width:242px;height:331px">
  <div class="card-media" style="left:50px;width:142px;background:linear-gradient(180deg,#d9ef1f,#c6e11c 60%,#8e9c2a)" role="img" aria-label="High visibility safety vest with printed message"></div>
  <h4>Product Heading</h4><div class="desc">Nulla luctus eget</div><div class="price">$10.00</div>
</div>
<div class="abs card" style="left:344px;top:2619px;width:242px;height:331px">
  <div class="card-media" style="background:linear-gradient(180deg,#c8202a 38%,#f4f4f4 38%,#e6e6e6)" role="img" aria-label="Printed floor sticker banner"></div>
  <h4>Product Heading</h4><div class="desc">Nulla luctus eget</div><div class="price">$10.00</div>
</div>
<div class="abs card" style="left:614px;top:2619px;width:242px;height:331px">
  <div class="card-media" style="background:linear-gradient(135deg,#2c4f9c,#5b7cc5 50%,#f1f1f1 70%)" role="img" aria-label="Hand holding a printed event flyer"></div>
  <h4>Product Heading</h4><div class="desc">Nulla luctus eget</div><div class="price">$10.00</div>
</div>
<div class="abs card" style="left:884px;top:2619px;width:241px;height:331px">
  <div class="card-media" style="background:linear-gradient(135deg,#d9a138,#e9bb52 55%,#c78f30)" role="img" aria-label="Printed beer mat coaster"></div>
  <h4>Product Heading</h4><div class="desc">Nulla luctus eget</div><div class="price">$10.00</div>
</div>

<h2 class="abs section-title" style="left:74px;top:3024px">LATEST FROM OUR BLOG</h2>
<article class="abs post" style="left:74px;top:3090px;width:512px;height:360px">
  <div class="post-media" style="background:linear-gradient(135deg,#2a2a2a,#6b6b6b 45%,#d8d8d8)" role="img" aria-label="Photo of a t-shirt being heat printed"></div>
  <h4>Duis a dolor elit</h4>
  <div class="post-meta"><span><svg width="13" height="13" viewBox="0 0 24 24"><rect x="2" y="4" width="20" height="18" fill="#21678f"/></svg>October 05, 2020</span><span><svg width="12" height="13" viewBox="0 0 24 24"><circle cx="12" cy="7" r="5" fill="#21678f"/><path d="M2 24c0-6 4-9 10-9s10 3 10 9z" fill="#21678f"/></svg>By Admin</span></div>
</article>
<article class="abs post" style="left:614px;top:3090px;width:511px;height:360px">
  <div class="post-media" style="background:linear-gradient(135deg,#2b3d86,#3550a3 40%,#c4202c 70%,#2a2a2a)" role="img" aria-label="Photo of a red t-shirt on a printing press"></div>
  <h4>Duis a dolor elit</h4>
  <div class="post-meta"><span><svg width="13" height="13" viewBox="0 0 24 24"><rect x="2" y="4" width="20" height="18" fill="#21678f"/></svg>October 05, 2020</span><span><svg width="12" height="13" viewBox="0 0 24 24"><circle cx="12" cy="7" r="5" fill="#21678f"/><path d="M2 24c0-6 4-9 10-9s10 3 10 9z" fill="#21678f"/></svg>By Admin</span></div>
</article>

<div class="abs map" role="img" aria-label="Street map showing the shop location"></div>
<div class="abs loc">
  <h3>LOCATIONS</h3>
  <div class="q">DO WE DELIVER TO YOUR AREA?</div>
  <div class="link">Find Out Here!</div>
  <div class="note">Orders placed before 12pm are<br>eligible for delivery in 1-2 working days</div>
  <div class="btn">GET DIRECTIONS</div>
</div>

<section class="abs news" role="img" aria-label="Photo of a designer's desk with a computer and pencils">
  <h2>STAY IN THE KNOW</h2>
  <p>Neque porro quisquam est qui dolorem ipsum quia dolor sit amet, consectetur, adipisci velit.</p>
</section>
<div class="abs news-field">Enter Email Addres</div>
<div class="abs news-go"><svg width="56" height="48" viewBox="0 0 56 48"><path d="M25 17l7 7-7 7" fill="none" stroke="#fff" stroke-width="3"/></svg></div>

<div class="abs perks">
  <div class="perk">LIGHTNING FAST<br>DELIVERY<svg width="36" height="36" viewBox="0 0 24 24"><path fill="#111" d="M21 16v-2l-8-5V3.5a1.5 1.5 0 00-3 0V9l-8 5v2l8-2.5V19l-2 1.5V22l3.5-1 3.5 1v-1.5L13 19v-5.5z"/></svg></div>
  <div class="perk">WORLDWIDE<br>SHIPPING<svg width="40" height="32" viewBox="0 0 30 22"><path fill="#111" d="M0 2h18v14H0zM19 6h6l5 5v5h-11z"/><circle cx="6" cy="18" r="3" fill="#111"/><circle cx="24" cy="18" r="3" fill="#111"/></svg></div>
  <div class="perk">24/7 TECHNICAL<br>SUPPORT<svg width="44" height="34" viewBox="0 0 30 22"><ellipse cx="11" cy="8" rx="11" ry="8" fill="#111"/><ellipse cx="20" cy="13" rx="10" ry="7" fill="#111"/><path d="M3 14l-2 6 7-3z" fill="#111"/></svg></div>
  <div class="perk">EASY RETURNS &amp;<br>EXCHANGES<svg width="36" height="36" viewBox="0 0 24 24"><path d="M20 10a8 8 0 00-15-3M4 14a8 8 0 0015 3" fill="none" stroke="#111" stroke-width="3"/><path d="M2 3v6h6zM22 21v-6h-6z" fill="#111"/></svg></div>
</div>

<div class="abs foot-col" style="left:75px;top:4450px">
  <h5>Navigation</h5>
  <ul><li>Home</li><li>About</li><li>Contact</li><li>Catalog</li><li>Shipping and Returns</li></ul>
</div>
<div class="abs foot-col" style="left:363px;top:4450px">
  <h5>Contact Info</h5>
  <p>48 Kerrow Street<br>Eastvale NSW 2010</p>
  <p style="margin-top:2px">Mon - Fri, 10am - 7pm</p>
</div>
<div class="abs foot-col" style="left:703px;top:4450px">
  <h5>Be in the know</h5>
  <p style="margin-bottom:12px">Promotions, new products and sales. Directly to your inbox.</p>
  <div class="foot-field">Enter Name<span class="go"><svg width="14" height="14" viewBox="0 0 24 24"><path d="M8 3l9 9-9 9" fill="none" stroke="#fff" stroke-width="3"/></svg></span></div>
  <div class="social"><i></i><i></i><i></i><i></i><i></i></div>
</div>

<div class="abs bottombar">
  <span>Copyright © 2021 Company Name All Right Reserved</span>
  <div class="pay"><i></i><i></i><i></i><i></i><i></i></div>
</div>

</body>
</html>
```